LinkedIn Banner Design for Asphalt & Parking Lot Company (Pavebright Dynamics LLC)

I need a professional LinkedIn banner designed for my company, Pavebright Dynamics LLC, based in Seattle. This banner should act as a visual “landing page header” for my profile and clearly communicate what we do within seconds.

The goal is to attract property managers, business owners, and commercial clients who are responsible for maintaining parking lots.

About the Business:
Pavebright Dynamics LLC provides asphalt parking lot services including:

Sealcoating
Crack sealing
Line striping
Asphalt maintenance & repair

Website: https://pavebrightdynamics.net
Location: Seattle, WA

Target Audience:

Property managers
Commercial real estate owners
Facility managers
Business owners with parking lots

Main Goal of the Banner:

Instantly show what we do
Build trust and professionalism
Generate leads from profile visitors
Make people think: “This is who I call for parking lot maintenance”

Headline / Tagline (Use This or Improve It):
Helping Property Managers Protect & Maintain Their Parking Lots

Subtext (optional but recommended):
Sealcoating • Crack Sealing • Line Striping

Design Style:

Clean, bold, and modern
Professional contractor/service look
High contrast and easy to read
Not cluttered

Branding / Colors:

Orange (primary accent color from logo)
Black / dark gray (asphalt tones)
White for contrast
Match branding from website and logo

Visual Direction (IMPORTANT):
Use high-quality, realistic images such as:

Freshly sealcoated, dark black parking lot
Clean, professionally striped parking lot
Before/after transformation (if done cleanly)

The banner should visually communicate:
“We make parking lots look new and last longer”

Focus more on RESULTS than workers.

Layout Notes:

Keep important text on the center/right side (profile photo covers left side)
Must look good on desktop and mobile
Avoid placing key elements on the far left

Optional Elements:

“Serving Seattle Area”
Website: pavebrightdynamics.net

Deliverables:

LinkedIn banner size: 1584 x 396 px
High-resolution file
Source file (PSD or AI)

What I DON’T Want:

Generic or low-quality stock designs
Overcrowded text
Cartoon-style construction graphics

Extra Notes:
This banner is important for lead generation. It should clearly communicate services even at a quick glance.

I’m open to creative ideas that align with attracting property managers and commercial clients.

Looking forward to your designs!

```html
<!DOCTYPE html>
<html lang="en">
<head>
<meta charset="utf-8">
<title>Pavebright Dynamics – LinkedIn Banner</title>
<link href="https://fonts.googleapis.com/css2?family=Roboto:ital,wght@0,500;0,700;1,900&display=swap" rel="stylesheet">
<style>
  :root {
    --page: #f9f9f9;
    --asphalt: #2d2c30;
    --orange: #f6830f;
    --white: #ffffff;
    --frame: #dcdcd9;
    --square-gray: #9a9a9a;
    --portrait-ring: #e6e6e6;
  }
  * { margin: 0; padding: 0; box-sizing: border-box; }
  html, body { width: 1200px; height: 1001px; overflow: hidden; background: var(--page); }
  body { position: relative; font-family: "Roboto", Arial, sans-serif; }

  .banner {
    position: absolute; left: 30px; top: 324px;
    width: 1139px; height: 284px;
    background: var(--asphalt);
  }
  .banner-graphics { position: absolute; inset: 0; width: 100%; height: 100%; }

  .dot-grid {
    position: absolute; left: 20px; top: 18px;
    display: grid; grid-template-columns: repeat(4, 10px);
    column-gap: 20px; row-gap: 14px;
  }
  .dot-grid span { width: 10px; height: 10px; background: var(--orange); }

  .pitch { position: absolute; left: 288px; top: 72px; color: var(--white); }
  .pitch-headline { font-weight: 700; font-size: 24px; line-height: 29px; }
  .pitch-services {
    margin-top: 14px; color: var(--orange);
    font-weight: 700; font-size: 13.5px; letter-spacing: 0.1px;
  }
  .pitch-website {
    margin-top: 26px; display: flex; align-items: center; gap: 5px;
    font-weight: 500; font-size: 26px;
  }
  .pitch-website svg { width: 21px; height: 21px; }

  .brand-name {
    position: absolute; left: 925px; top: 176px; width: 190px;
    color: var(--white); font-weight: 700; font-size: 24px; line-height: 27px;
    text-align: center;
  }

  .portrait {
    position: absolute; left: 61px; top: 448px;
    width: 228px; height: 228px; border-radius: 50%;
    border: 6px solid var(--portrait-ring);
    background: radial-gradient(circle at 50% 40%, #c9c9c9, #8a8a8a);
  }
</style>
</head>
<body>
  <section class="banner">
    <svg class="banner-graphics" viewBox="0 0 1423 355" preserveAspectRatio="none">
      <defs>
        <linearGradient id="worn-asphalt" x1="0" y1="0" x2="1" y2="1">
          <stop offset="0" stop-color="#6f6a63"/>
          <stop offset="0.5" stop-color="#8a7660"/>
          <stop offset="1" stop-color="#4b4742"/>
        </linearGradient>
        <linearGradient id="fresh-asphalt" x1="0" y1="0" x2="1" y2="1">
          <stop offset="0" stop-color="#4d5a52"/>
          <stop offset="0.35" stop-color="#26282c"/>
          <stop offset="1" stop-color="#15161a"/>
        </linearGradient>
      </defs>

      <polygon points="930,0 1252,0 1360,192 1057,192" fill="var(--frame)"/>
      <polygon class="photo-before" role="img" aria-label="Photo of a cracked parking lot with a water-filled pothole"
               points="952,0 1227,0 1330,178 1082,178" fill="url(#worn-asphalt)"/>

      <polygon points="787,163 1092,163 1217,355 932,355" fill="var(--frame)"/>
      <polygon class="photo-after" role="img" aria-label="Photo of a freshly sealcoated parking lot with new yellow striping"
               points="820,178 1100,178 1200,355 945,355" fill="url(#fresh-asphalt)"/>

      <path d="M955,53 C912,68 900,118 918,146" fill="none" stroke="var(--orange)" stroke-width="4" stroke-linecap="round"/>
      <path d="M905,126 L918,150 L928,124" fill="none" stroke="var(--orange)" stroke-width="4" stroke-linecap="round" stroke-linejoin="round"/>

      <polygon points="1163,0 1270,0 1266,33 1159,33" fill="var(--orange)"/>
      <text x="1215" y="27" text-anchor="middle" font-family="Roboto, Arial, sans-serif" font-style="italic" font-weight="900" font-size="27" fill="#2d2c30">Before</text>
      <polygon points="955,322 1060,322 1058,355 952,355" fill="var(--orange)"/>
      <text x="1006" y="349" text-anchor="middle" font-family="Roboto, Arial, sans-serif" font-style="italic" font-weight="900" font-size="27" fill="#2d2c30">After</text>

      <g fill="var(--square-gray)">
        <rect x="1375" y="237" width="11" height="11"/>
        <rect x="1375" y="266" width="11" height="11"/>
        <rect x="1375" y="295" width="11" height="11"/>
        <rect x="1375" y="324" width="11" height="11"/>
        <rect x="1267" y="324" width="11" height="11"/>
        <rect x="1303" y="324" width="11" height="11"/>
        <rect x="1339" y="324" width="11" height="11"/>
      </g>
    </svg>

    <div class="dot-grid">
      <span></span><span></span><span></span><span></span>
      <span></span><span></span><span></span><span></span>
      <span></span><span></span><span></span><span></span>
      <span></span><span></span><span></span><span></span>
    </div>

    <div class="pitch">
      <h1 class="pitch-headline">Helping Property Managers<br>Protect &amp; Maintain Their<br>Parking Lots</h1>
      <p class="pitch-services">SEALCOATING · CRACK SEALING · LINE STRIPING</p>
      <p class="pitch-website">
        <svg viewBox="0 0 24 24" fill="none" stroke="var(--orange)" stroke-width="2">
          <circle cx="12" cy="12" r="10"/>
          <ellipse cx="12" cy="12" rx="4.5" ry="10"/>
          <line x1="2" y1="12" x2="22" y2="12"/>
          <line x1="4" y1="7" x2="20" y2="7"/>
          <line x1="4" y1="17" x2="20" y2="17"/>
        </svg>
        pavebrightdynamics.net
      </p>
    </div>

    <p class="brand-name">Pavebright<br>Dynamics</p>
  </section>

  <div class="portrait" role="img" aria-label="Profile photo of the company owner"></div>
</body>
</html>
```